Meridale Cleaning Services

In need of a business card design suited for a growing cleaning company.

We offer our cleaning and maintenance services to a wide range of clients including but not limited to the following: constuction industry, hospitality, commercial, industrial and domestic

I want the card to be very noticable, i would like people to say 'hey, great card!' when i hand them my card.double sided would be nice

we want our business to come across as exceedingly professional and innovative (different).

a contemporary design is what we have in mind
we want to present an image of a quality business with a high standard of excellence in consistent service.

i just really need a card that persuades top end quality,
our business is very certified and also strives towards environmentaly friendly alternatives
Updates

hey sorry, i have uploaded my company logo design and name
cheers.

hey guys i have added my company logo/name file on my brief page. many thanks

sorry guys a typo in the brief..
address is Tolley Rd. not Tolly Rd
thanks

Industry/Entity Type

Industrial

Requirements
Must have
• company name: meridale cleaning services
operations manager: Colm Varetti
Tel: (02)9373 6204
Fax: (02)8645 7712
Mob: 0438571490

address: 47 Tolly RD Kelvale NSW 2081
Postal Adress: PO Box 5832 Westbrook NSW 2126
email: meridaleclean@wexanet.com.au
website: meridalecleaningservices.com.au

```html
<!DOCTYPE html>
<html lang="en">
<head>
<meta charset="utf-8">
<title>Meridale Cleaning Services – Business Card</title>
<link href="https://fonts.googleapis.com/css2?family=Source+Sans+3:wght@400;600;700&display=swap" rel="stylesheet">
<style>
  :root {
    --page: #ffffff;
    --card: #ffffff;
    --card-edge: #dcdcdc;
    --brand-blue: #1b74c4;
    --brand-blue-deep: #0d4f9a;
    --brand-blue-light: #3fa0e6;
    --leaf-green: #8cc63f;
    --leaf-green-deep: #4f9a2a;
    --leaf-green-light: #b8df6a;
    --ink: #222222;
    --ink-soft: #6a6a6a;
  }
  html, body {
    margin: 0;
    padding: 0;
    background: var(--page);
    overflow: hidden;
  }
  .canvas {
    position: relative;
    width: 1200px;
    height: 332px;
    overflow: hidden;
    background: var(--page);
    font-family: "Source Sans 3", "Myriad Pro", Arial, sans-serif;
  }
  .card {
    position: absolute;
    top: 22px;
    width: 558px;
    height: 288px;
    background: var(--card);
    border: 1px solid var(--card-edge);
    box-shadow: 2px 3px 6px rgba(0,0,0,0.18);
    overflow: hidden;
  }
  .card--front { left: 17px; }
  .card--back { left: 625px; }
  .accent-band {
    position: absolute;
    top: 0;
    bottom: 0;
  }
  .accent-band--front {
    right: 0;
    width: 70px;
    background: linear-gradient(180deg, var(--brand-blue-deep), var(--brand-blue-light) 55%, var(--leaf-green));
  }
  .accent-band--back-left {
    left: 0;
    width: 56px;
    background: linear-gradient(180deg, var(--brand-blue-light), var(--brand-blue-deep));
  }
  .accent-band--back-right {
    right: 0;
    width: 56px;
    background: linear-gradient(180deg, var(--leaf-green-light), var(--leaf-green-deep));
  }
  .brand {
    position: absolute;
    left: 120px;
    top: 104px;
    display: flex;
    align-items: center;
    gap: 12px;
    color: var(--brand-blue);
    font-weight: 700;
  }
  .brand__dot {
    width: 56px;
    height: 56px;
    border-radius: 50%;
    background: var(--brand-blue);
    flex: none;
  }
  .brand__name {
    line-height: 1;
  }
  .brand__main {
    display: block;
    font-size: 36px;
    letter-spacing: -0.5px;
  }
  .brand__sub {
    display: block;
    font-size: 12px;
    letter-spacing: 1px;
    text-transform: uppercase;
    margin-top: 3px;
  }
  .contact {
    position: absolute;
    left: 150px;
    top: 16px;
    color: var(--ink-soft);
    font-size: 16px;
    line-height: 21px;
  }
  .contact__name {
    color: var(--brand-blue);
    font-size: 23px;
    line-height: 26px;
    margin: 0;
    font-weight: 400;
  }
  .contact__role {
    color: var(--ink);
    font-size: 17px;
    margin: 0 0 2px;
  }
  .contact__lines, .contact__address {
    margin: 0;
  }
  .contact__address {
    margin-top: 16px;
  }
</style>
</head>
<body>
<div class="canvas">

  <section class="card card--front">
    <div class="accent-band accent-band--front" role="img" aria-label="Decorative blue and green colour band"></div>
    <div class="brand">
      <span class="brand__dot"></span>
      <span class="brand__name">
        <span class="brand__main">Meridale</span>
        <span class="brand__sub">Cleaning Services</span>
      </span>
    </div>
  </section>

  <section class="card card--back">
    <div class="accent-band accent-band--back-left" role="img" aria-label="Decorative blue colour band"></div>
    <div class="accent-band accent-band--back-right" role="img" aria-label="Decorative green colour band"></div>
    <div class="contact">
      <h1 class="contact__name">Colm Varetti</h1>
      <p class="contact__role">operations manager</p>
      <p class="contact__lines">Tel: (02)9373 6204<br>Fax: (02)8645 7712<br>Mob: 0438571490</p>
      <p class="contact__address">47 Tolly RD Kelvale NSW 2081<br>PO Box 5832 Westbrook NSW 2126<br>meridaleclean@wexanet.com.au<br>www.meridalecleaningservices.com.au</p>
    </div>
  </section>

</div>
</body>
</html>
```